Road Construction Company needs business cards

We would like a new business card designed for our business.

We're a road construction company based in Qld, Australia.

Can the business card please have the following information on it.

Name: Brent Malvoy
Position: General Manager
Phone: 0471 592 304
Email: Brent.malvoy@quendix.com.au
Address: 87 Harrowgate Ave, Pindarra, QLD, 4000
Website: www.quendix.com.au

Visually we'd like the card to be professional and simple.

Attached is our logo.

Our website is www.quendix.com.au

Target Market(s)

Men aged 25-60

Contact Information for Business Card

As listed in project description

Font styles to use
Serif

Requirements
Must have
• Large logo on back of card

```html
<!DOCTYPE html>
<html lang="en">
<head>
<meta charset="utf-8">
<title>Quendix Road Construction – Business Card</title>
<link href="https://fonts.googleapis.com/css2?family=Montserrat:wght@400;500;700;800&display=swap" rel="stylesheet">
<style>
  :root{
    --stage:#1158f5;
    --card-white:#ffffff;
    --card-dark:#12151a;
    --brand-blue:#1a5cf0;
    --sky:#4cc8ee;
    --ink:#1f2226;
    --road-tone:#d9dcdf;
    --pattern-tone:#1a2130;
  }
  *{margin:0;padding:0;box-sizing:border-box}
  html,body{width:960px;height:1200px;overflow:hidden;background:var(--stage)}
  body{position:relative;font-family:"Montserrat",Arial,sans-serif;color:var(--ink)}

  .card{position:absolute;left:61px;width:839px;height:480px;border-radius:48px;overflow:hidden;
        box-shadow:0 14px 30px rgba(0,20,90,.35)}
  .card--front{top:76px;background:var(--card-white)}
  .card--back{top:644px;background:var(--card-dark)}

  .road-art{position:absolute;left:0;top:0;width:560px;height:480px;
            background:linear-gradient(90deg,var(--road-tone) 0%,#eceef0 55%,var(--card-white) 100%)}

  .divider{position:absolute;left:628px;top:0;height:480px;width:4px}

  .wordmark{position:absolute;font-weight:800;line-height:1;white-space:nowrap}
  .tagline{position:absolute;font-weight:700;color:var(--sky);line-height:1;white-space:nowrap}

  .card--front .wordmark{left:44px;top:200px;font-size:62px;letter-spacing:6px;color:var(--brand-blue)}
  .card--front .tagline{left:46px;top:263px;font-size:14px;letter-spacing:12.4px}

  .person-icon{position:absolute;left:612px;top:48px}
  .identity{position:absolute;left:500px;width:260px;top:89px;text-align:center}
  .identity .name{font-size:26px;color:var(--brand-blue);font-weight:500;line-height:1;letter-spacing:.3px}
  .identity .name b{font-weight:800}
  .identity .role{margin-top:2px;font-size:14px;letter-spacing:5px;font-weight:500;padding-left:5px}

  .contact-icons{position:absolute;left:574px;top:316px;display:flex;gap:7px}
  .contacts{position:absolute;left:400px;width:458px;top:346px;text-align:center;list-style:none;
            font-size:18.5px;line-height:25.6px;font-weight:400}

  .back-texture{position:absolute;inset:0;
                background:radial-gradient(ellipse at 50% 30%,var(--pattern-tone) 0%,var(--card-dark) 75%)}
  .card--back .wordmark{left:0;width:839px;text-align:center;top:170px;font-size:108px;letter-spacing:9px;padding-left:9px;color:#fff}
  .card--back .tagline{left:0;width:839px;text-align:center;top:284px;font-size:24px;letter-spacing:15px;padding-left:15px}
</style>
</head>
<body>

<section class="card card--front">
  <div class="road-art" role="img" aria-label="Winding road illustration curving down the left side of the card"></div>

  <svg class="divider" width="4" height="480" aria-hidden="true">
    <line x1="2" y1="0" x2="2" y2="42" stroke="var(--brand-blue)" stroke-width="3" stroke-dasharray="9 8"/>
    <line x1="2" y1="142" x2="2" y2="310" stroke="var(--brand-blue)" stroke-width="3" stroke-dasharray="9 8"/>
    <line x1="2" y1="468" x2="2" y2="480" stroke="var(--brand-blue)" stroke-width="3"/>
  </svg>

  <div class="wordmark">QUENDIX</div>
  <div class="tagline">ROAD CONSTRUCTION</div>

  <svg class="person-icon" width="34" height="40" viewBox="0 0 34 40" aria-hidden="true">
    <circle cx="17" cy="9" r="8" fill="var(--brand-blue)"/>
    <path d="M2 40 V27 Q2 20 10 19 L17 28 L24 19 Q32 20 32 27 V40 Z" fill="var(--brand-blue)"/>
    <path d="M15.5 21 L18.5 21 L19 31 L17 34 L15 31 Z" fill="#fff"/>
  </svg>

  <div class="identity">
    <p class="name"><b>BRENT</b> MALVOY</p>
    <p class="role">GENERAL MANAGER</p>
  </div>

  <div class="contact-icons" aria-hidden="true">
    <svg width="24" height="24" viewBox="0 0 24 24"><path d="M5 2 L9 2 L10.5 7 L8 9 Q10 14 15 16 L17 13.5 L22 15 L22 19 Q22 22 19 22 Q3 20 2 5 Q2 2 5 2Z" fill="var(--brand-blue)"/><path d="M14 2 A8 8 0 0 1 22 10 M14 6 A4 4 0 0 1 18 10" stroke="var(--brand-blue)" stroke-width="2" fill="none"/></svg>
    <svg width="26" height="24" viewBox="0 0 26 24"><rect x="1" y="3" width="20" height="14" rx="1.5" fill="var(--brand-blue)"/><path d="M1 4 L11 11 L21 4" stroke="#fff" stroke-width="1.6" fill="none"/><circle cx="20" cy="18" r="5" fill="#fff" stroke="var(--brand-blue)" stroke-width="2"/><circle cx="20" cy="18" r="1.8" fill="var(--brand-blue)"/></svg>
    <svg width="20" height="24" viewBox="0 0 20 24"><path d="M10 1 A8 8 0 0 1 18 9 C18 15 10 23 10 23 C10 23 2 15 2 9 A8 8 0 0 1 10 1Z" fill="var(--brand-blue)"/><circle cx="10" cy="9" r="3" fill="#fff"/></svg>
    <svg width="24" height="24" viewBox="0 0 24 24"><circle cx="12" cy="12" r="11" fill="var(--brand-blue)"/><g stroke="#fff" stroke-width="1.4" fill="none"><ellipse cx="12" cy="12" rx="4.5" ry="10.5"/><line x1="1" y1="12" x2="23" y2="12"/><line x1="12" y1="1" x2="12" y2="23"/><path d="M3 7 H21 M3 17 H21"/></g></svg>
  </div>

  <ul class="contacts">
    <li>0471 592 304</li>
    <li>Brent.malvoy@quendix.com.au</li>
    <li>87 Harrowgate Ave, Pindarra, QLD, 4000</li>
    <li>www.quendix.com.au</li>
  </ul>
</section>

<section class="card card--back">
  <div class="back-texture" role="img" aria-label="Faint repeating arrow pattern in dark navy across the background"></div>
  <div class="wordmark">QUENDIX</div>
  <div class="tagline">ROAD CONSTRUCTION</div>
</section>

</body>
</html>
```